Ledgerwise Business Card Design

Business Card Design for new business called Ledgerwise focused on selling business software to small and medium size companies who have outgrown Tallymark. Similar companies would be Tallymark, Nuvo, CoreFlow. Also Dealharbor would be good to look at for additional ideas around look and feel.

Target Market(s)

Business to Business

Industry/Entity Type

Information Technology

Contact Information for Business Card

Standard Business Card Information

Font styles to use
Sans Serif

```html
<!DOCTYPE html>
<html lang="en">
<head>
<meta charset="utf-8">
<title>Ledgerwise Business Card</title>
<link rel="stylesheet" href="https://fonts.googleapis.com/css2?family=Montserrat:wght@700&family=Open+Sans:wght@400;600&display=swap">
<style>
  :root {
    --page-bg: #ece9e6;
    --brand-blue: #1a5286;
    --band-blue-light: #2c7fbd;
    --band-blue-dark: #0f4d85;
    --brand-orange: #f7821a;
    --orange-light: #fb9a2e;
    --white: #ffffff;
    --rule: rgba(255,255,255,0.55);
  }
  html, body {
    margin: 0;
    width: 1200px;
    height: 900px;
    overflow: hidden;
    background: var(--page-bg);
    font-family: "Open Sans", sans-serif;
  }
  .canvas { position: relative; width: 1200px; height: 900px; }
  .card {
    position: absolute;
    overflow: hidden;
    box-shadow: 0 6px 18px rgba(0,0,0,0.18);
  }
  /* Front */
  .card-front { left: 237px; top: 62px; width: 556px; height: 343px; background: var(--white); }
  .front-logo-area {
    position: absolute; left: 0; top: 0; width: 100%; height: 181px;
    display: flex; align-items: center; justify-content: center; gap: 14px;
  }
  .wordmark {
    font-family: "Montserrat", sans-serif;
    font-weight: 700;
    letter-spacing: 0.5px;
    margin: 0;
  }
  .front-logo-area .wordmark { font-size: 40px; color: var(--brand-blue); }
  .logo-dot { width: 26px; height: 26px; border-radius: 50%; background: var(--brand-orange); }
  .front-rule { position: absolute; left: 0; top: 181px; width: 100%; height: 7px; background: var(--brand-orange); }
  .front-band {
    position: absolute; left: 0; top: 188px; width: 100%; height: 155px;
    background: linear-gradient(180deg, var(--band-blue-light) 0%, var(--band-blue-light) 40%, var(--band-blue-dark) 75%);
    color: var(--white);
  }
  .person {
    position: absolute; right: 277px; top: 20px; text-align: right;
  }
  .person-name { font-size: 18px; font-weight: 600; margin: 0; line-height: 24px; }
  .person-title { font-size: 14.5px; margin: 0 0 10px; line-height: 20px; }
  .person-address { font-size: 14.5px; margin: 0; line-height: 20px; }
  .contacts { position: absolute; left: 294px; top: 22px; margin: 0; padding: 0; list-style: none; }
  .contacts li { display: flex; align-items: center; gap: 8px; font-size: 14.5px; height: 23px; }
  .contacts svg { width: 12px; height: 12px; fill: var(--white); }
  /* Back */
  .card-back {
    left: 459px; top: 518px; width: 560px; height: 343px;
    background: linear-gradient(180deg, var(--brand-orange) 0%, var(--orange-light) 55%);
  }
  .back-band {
    position: absolute; left: 0; top: 187px; width: 100%; height: 156px;
    background: linear-gradient(180deg, var(--band-blue-light) 0%, var(--band-blue-light) 45%, var(--band-blue-dark) 85%);
  }
  .back-wordmark {
    position: absolute; left: 0; top: 130px; width: 100%;
    text-align: center; font-size: 50px; color: var(--white); line-height: 60px;
  }
  .back-footer {
    position: absolute; left: 0; top: 300px; width: 100%;
    display: flex; align-items: center; gap: 12px; color: var(--white);
    font-size: 14.5px; font-weight: 600;
  }
  .back-footer .line { flex: 1; height: 1px; background: var(--rule); }
</style>
</head>
<body>
<main class="canvas">
  <section class="card card-front" aria-label="Business card front">
    <div class="front-logo-area">
      <span class="logo-dot" aria-hidden="true"></span>
      <h1 class="wordmark">LEDGERWISE</h1>
    </div>
    <div class="front-rule"></div>
    <div class="front-band">
      <div class="person">
        <p class="person-name">Daniel Reyes</p>
        <p class="person-title">Managing Director</p>
        <p class="person-address">12345, Address Goes Here</p>
        <p class="person-address">Country Name, 123456.</p>
      </div>
      <ul class="contacts">
        <li><svg viewBox="0 0 24 24" aria-hidden="true"><path d="M6.6 10.8a15 15 0 0 0 6.6 6.6l2.2-2.2c.3-.3.7-.4 1-.2 1.1.4 2.3.6 3.6.6.6 0 1 .4 1 1V20c0 .6-.4 1-1 1A17 17 0 0 1 3 4c0-.6.4-1 1-1h3.5c.6 0 1 .4 1 1 0 1.3.2 2.5.6 3.6.1.3 0 .7-.2 1z"/></svg>044-123 456 789</li>
        <li><svg viewBox="0 0 24 24" aria-hidden="true"><path d="M6 2h9l3 3v5h2a2 2 0 0 1 2 2v10H2V12a2 2 0 0 1 2-2h2zm2 2v6h8V6h-3V4zm-2 10v2h3v-2zm5 0v2h3v-2zm5 0v2h3v-2zM6 18v2h3v-2zm5 0v2h3v-2zm5 0v2h3v-2z"/></svg>044-123 456 789</li>
        <li><svg viewBox="0 0 24 24" aria-hidden="true"><path d="M2 5h20v14H2zm2 2v.5l8 5 8-5V7zm0 2.8V17h16V9.8l-8 5z"/></svg>info@webname.com</li>
        <li><svg viewBox="0 0 24 24" aria-hidden="true"><path d="M12 2a10 10 0 1 0 0 20 10 10 0 0 0 0-20zm6.9 9h-3a15 15 0 0 0-1.3-5.6A8 8 0 0 1 18.9 11zM12 4.1c.9 1.2 1.8 3.6 1.9 6.9h-3.8c.1-3.3 1-5.7 1.9-6.9zM9.4 5.4A15 15 0 0 0 8.1 11h-3a8 8 0 0 1 4.3-5.6zM5.1 13h3a15 15 0 0 0 1.3 5.6A8 8 0 0 1 5.1 13zm6.9 6.9c-.9-1.2-1.8-3.6-1.9-6.9h3.8c-.1 3.3-1 5.7-1.9 6.9zm2.6-1.3a15 15 0 0 0 1.3-5.6h3a8 8 0 0 1-4.3 5.6z"/></svg>www.website.com</li>
      </ul>
    </div>
  </section>

  <section class="card card-back" aria-label="Business card back">
    <div class="back-band"></div>
    <h2 class="wordmark back-wordmark">LEDGERWISE</h2>
    <div class="back-footer">
      <span class="line"></span>
      <span class="site">www.website.com</span>
      <span class="line"></span>
    </div>
  </section>
</main>
</body>
</html>
```